Onboarding project UI redesign

The web site is used to onboard clients via a video-identification process.
The end-user first tests his computer, then enters his order details and waits for an operator engagement.
When the operator engages the customer, they go through some identification steps together, ending on a contract signature page.

Target Market(s)

Finance B2C

Industry/Entity Type

Finance

Coding

Coded - Design and coding required

Number of Pages Required

5+ page

Font styles to use
Sans Serif

Requirements
Must have
• Professional UI
• Design for mobile devices

```html
<!DOCTYPE html>
<html lang="en">
<head>
<meta charset="utf-8">
<title>Norvelle Bank – Video Identification</title>
<link rel="stylesheet" href="https://fonts.googleapis.com/css2?family=Roboto:wght@400;500;700&display=swap">
<style>
  :root {
    --brand-blue: #084b8e;
    --title-blue: #0b57a4;
    --text-dark: #222222;
    --text-muted: #8a8a8a;
    --panel-bg: #f5f5f5;
    --white: #ffffff;
    --ring-track: #e2e2e2;
    --accent-green: #76b52a;
    --pill-grey: #a9a9a9;
    --pill-dot: #6f6f6f;
  }
  * { box-sizing: border-box; margin: 0; padding: 0; }
  html, body { width: 1200px; height: 675px; overflow: hidden; }
  body {
    font-family: "Roboto", Arial, sans-serif;
    background: var(--panel-bg);
    color: var(--text-dark);
    position: relative;
  }

  .top-bar {
    position: absolute; left: 0; top: 0; width: 1200px; height: 44px;
    background: var(--brand-blue);
    display: flex; align-items: center; justify-content: space-between;
    padding: 0 44px;
  }
  .brand { display: flex; align-items: center; }
  .brand-name {
    color: var(--white);
    font-size: 15px; font-weight: 500; line-height: 1; letter-spacing: 0.3px;
    white-space: nowrap;
  }
  .clock { color: var(--white); font-size: 11px; display: flex; gap: 13px; }
  .clock-time { font-weight: 700; }

  .step-header {
    position: absolute; left: 0; top: 44px; width: 1200px; height: 66px;
    background: var(--white);
    box-shadow: 0 2px 6px rgba(0,0,0,0.12);
    z-index: 2;
  }
  .step-progress { position: absolute; left: 44px; top: 7px; width: 52px; height: 52px; }
  .step-progress-label {
    position: absolute; inset: 0; display: flex; align-items: center; justify-content: center;
    font-size: 15px; font-weight: 700; color: var(--text-dark);
  }
  .step-progress-label small { font-size: 10px; font-weight: 400; color: var(--text-muted); margin-left: 1px; margin-top: 3px; }
  .step-text { position: absolute; left: 119px; top: 20px; }
  .step-number { font-size: 10px; color: var(--text-dark); }
  .step-title { font-size: 12px; font-weight: 700; color: var(--title-blue); margin-top: 5px; letter-spacing: 0.1px; white-space: nowrap; }

  .operator { position: absolute; right: 44px; top: 10px; display: flex; align-items: center; gap: 14px; }
  .operator-info { text-align: right; }
  .operator-name { font-size: 12px; font-weight: 700; white-space: nowrap; }
  .operator-role { font-size: 10px; color: var(--text-muted); margin-top: 3px; }
  .operator-avatar {
    width: 46px; height: 46px; border-radius: 50%;
    background: radial-gradient(circle at 50% 40%, #d9b39a 0%, #b98c72 45%, #d8dcdf 70%);
  }

  .customer-video {
    position: absolute; left: 0; top: 110px; width: 543px; height: 565px;
    background: linear-gradient(180deg, #f7ede3 0%, #e4d8cc 45%, #2b4670 80%, #1f3a63 100%);
  }
  .record-pill {
    position: absolute; left: 416px; top: 22px; width: 105px; height: 31px;
    background: var(--pill-grey); border-radius: 2px;
    display: flex; align-items: center; justify-content: center; gap: 7px;
    color: var(--white); font-size: 12px; font-weight: 700;
  }
  .record-dot { width: 14px; height: 14px; border-radius: 50%; background: var(--pill-dot); }
  .operator-video {
    position: absolute; left: 21px; top: 424px; width: 119px; height: 120px;
    border: 2px solid var(--title-blue);
    background: linear-gradient(160deg, #e9eef2 0%, #c9b2a2 50%, #eef0f1 100%);
  }

  .instruction-panel {
    position: absolute; left: 543px; top: 110px; width: 657px; height: 565px;
    background: var(--panel-bg);
  }
  .instruction-text {
    position: absolute; left: 0; width: 657px; top: 240px;
    text-align: center; font-size: 15px; color: var(--text-dark);
  }
  .confirm-button {
    position: absolute; left: 269px; top: 292px; width: 119px; height: 31px;
    background: var(--accent-green); color: var(--white);
    border: none; border-radius: 2px;
    font-family: "Roboto", Arial, sans-serif; font-size: 11px; font-weight: 700;
  }
  .chat-button {
    position: absolute; left: 582px; top: 516px; width: 31px; height: 31px;
    border-radius: 50%; background: var(--accent-green);
    display: flex; align-items: center; justify-content: center;
  }
</style>
</head>
<body>
  <header class="top-bar">
    <div class="brand">
      <span class="brand-name">NORVELLE BANK</span>
    </div>
    <div class="clock">
      <span class="clock-date">Friday, March 22, 2019</span>
      <span class="clock-time">11:12 AM</span>
    </div>
  </header>

  <section class="step-header">
    <div class="step-progress">
      <svg width="52" height="52" viewBox="0 0 52 52">
        <circle cx="26" cy="26" r="24" fill="none" stroke="var(--ring-track)" stroke-width="3"/>
        <circle cx="26" cy="26" r="24" fill="none" stroke="var(--accent-green)" stroke-width="3"
                stroke-dasharray="13.7 150.8" transform="rotate(-90 26 26)"/>
      </svg>
      <div class="step-progress-label">1<small>/11</small></div>
    </div>
    <div class="step-text">
      <p class="step-number">Step 1.</p>
      <p class="step-title">CONFIRM QUALITY OF CONNECTION AND COMMUNICATION</p>
    </div>
    <div class="operator">
      <div class="operator-info">
        <p class="operator-name">Daniel Moreau</p>
        <p class="operator-role">Operator</p>
      </div>
      <div class="operator-avatar" role="img" aria-label="Operator profile photo"></div>
    </div>
  </section>

  <main>
    <section class="customer-video" role="img" aria-label="Live video feed of the customer">
      <div class="record-pill"><span class="record-dot"></span>00:00:00</div>
      <div class="operator-video" role="img" aria-label="Live video feed of the operator wearing a headset"></div>
    </section>

    <section class="instruction-panel">
      <p class="instruction-text">In order to complete this process, keep your identity document ready.</p>
      <button class="confirm-button">CONFIRM</button>
      <div class="chat-button" aria-label="Open chat">
        <svg width="18" height="16" viewBox="0 0 18 16">
          <path d="M7 1.5c3.3 0 6 2 6 4.6S10.3 10.7 7 10.7c-.6 0-1.2-.1-1.8-.2L2.3 12l.8-2.5C1.8 8.7 1 7.5 1 6.1 1 3.5 3.7 1.5 7 1.5z" fill="var(--white)"/>
          <path d="M14.2 5.3c1.7.8 2.8 2.1 2.8 3.7 0 1.1-.6 2.1-1.5 2.9l.6 2.1-2.4-1.2c-.5.1-1 .2-1.6.2-1.6 0-3-.5-4-1.3 3.4-.2 6.1-2.6 6.1-5.5v-.9z" fill="var(--white)"/>
        </svg>
      </div>
    </section>
  </main>
</body>
</html>
```